One of a Kind Clean Business Card

We need to design a new business card template for our company. Our company designs and produced merchandising displays. You can see a sample of what we produce on our site www.qorvatfixtures.com. I have uploaded our logo in vector format, as well as a picture of our current business cards. We want a totally different look. We want simple and clean, looking forward to seeing what people create.
Updates

I would like to update the address for Tellur Works 418 N Brindle Ave Fernhollow, WI 60817 Would also note. No QR codes

Industry/Entity Type

Business

Contact Information for Business Card

Need a 1 sided business card designed.

Font styles to use
Serif

Requirements
Must have
• Easy to view; Clean Design
Nice to have
• Features that promote engineering and creativity
Should not have
• Too much clutter, keep it simple

```html
<!DOCTYPE html>
<html lang="en">
<head>
<meta charset="utf-8">
<title>Tellur Works – Business Card</title>
<link href="https://fonts.googleapis.com/css2?family=Arimo:wght@400;700&display=swap" rel="stylesheet">
<style>
  :root {
    --backdrop: #3a3a3a;
    --card: #f7f7f7;
    --card-shade: #e9e9e9;
    --ink: #1c1c1c;
    --brand-red: #8e1217;
    --tile-edge: #111111;
    --white: #ffffff;
  }
  * { margin: 0; padding: 0; box-sizing: border-box; }
  html, body {
    width: 1200px; height: 997px; overflow: hidden;
    background: var(--backdrop);
    font-family: "Arimo", Arial, sans-serif;
  }
  .business-card {
    position: absolute; left: 100px; top: 213px;
    width: 1000px; height: 572px;
    background: linear-gradient(135deg, var(--white) 0%, var(--card) 60%, var(--card-shade) 100%);
    overflow: hidden;
    box-shadow: 0 18px 40px rgba(0,0,0,.45);
  }
  .product-tiles { position: absolute; left: 0; top: 0; width: 480px; height: 572px; }

  .brand-block {
    position: absolute; left: 560px; top: 78px; width: 380px;
    display: flex; align-items: center; gap: 14px;
  }
  .brand-mark { width: 20px; height: 20px; background: var(--ink); flex: none; }
  .brand-name {
    font-size: 38px; font-weight: 400; color: var(--ink);
    line-height: 1; white-space: nowrap;
  }

  .name-band {
    position: absolute; right: 0; top: 156px; width: 290px; height: 64px;
    background: var(--brand-red); border-radius: 14px 0 0 14px;
    color: var(--white); text-align: center; padding-top: 6px;
  }
  .person-name { font-size: 28px; font-weight: 700; letter-spacing: .5px; }
  .person-role { font-size: 19px; color: #f2d9da; }

  .contact-details {
    position: absolute; right: 110px; top: 258px; text-align: right;
    color: var(--ink); font-size: 24px; line-height: 32px;
  }
  .address { margin-bottom: 28px; }
  .email { margin-top: 22px; }

  .icon-rail {
    position: absolute; right: 62px; top: 340px; width: 38px; height: 130px;
    background: var(--brand-red); border-radius: 19px;
    display: flex; flex-direction: column; align-items: center; justify-content: space-evenly;
  }

  .web-pill {
    position: absolute; right: 36px; top: 506px; height: 34px; padding: 0 26px;
    background: var(--brand-red); border-radius: 17px 17px 0 17px;
    color: var(--white); font-size: 22px; font-weight: 700; line-height: 34px;
  }
  .base-stripe {
    position: absolute; left: 420px; right: 0; bottom: 18px; height: 14px;
    background: var(--brand-red);
  }
</style>
</head>
<body>
  <div class="business-card">
    <svg class="product-tiles" viewBox="0 0 480 572" role="img" aria-label="Six product photographs of merchandising displays: shelf trays, a counter box, a hanging rack, a wooden barrel, a refrigerated case and a snack stand">
      <defs>
        <linearGradient id="tileFill" x1="0" y1="0" x2="1" y2="1">
          <stop offset="0" stop-color="#c9b7a2"/>
          <stop offset="1" stop-color="#8a5a3c"/>
        </linearGradient>
        <linearGradient id="tileFillRed" x1="0" y1="0" x2="1" y2="1">
          <stop offset="0" stop-color="#e7d3d3"/>
          <stop offset="1" stop-color="#a4262b"/>
        </linearGradient>
        <linearGradient id="tileFillCool" x1="0" y1="0" x2="1" y2="1">
          <stop offset="0" stop-color="#b9c2cc"/>
          <stop offset="1" stop-color="#4d5560"/>
        </linearGradient>
      </defs>
      <g stroke="var(--tile-edge)" stroke-width="3">
        <rect x="-65" y="-65" width="130" height="130" rx="22" transform="translate(60 70) rotate(45)" fill="url(#tileFillCool)"/>
        <rect x="-65" y="-65" width="130" height="130" rx="22" transform="translate(205 172) rotate(45)" fill="url(#tileFillRed)"/>
        <rect x="-65" y="-65" width="130" height="130" rx="22" transform="translate(350 274) rotate(45)" fill="url(#tileFillRed)"/>
        <rect x="-65" y="-65" width="130" height="130" rx="22" transform="translate(60 296) rotate(45)" fill="url(#tileFill)"/>
        <rect x="-65" y="-65" width="130" height="130" rx="22" transform="translate(205 398) rotate(45)" fill="url(#tileFillCool)"/>
        <rect x="-65" y="-65" width="130" height="130" rx="22" transform="translate(350 500) rotate(45)" fill="url(#tileFill)"/>
      </g>
    </svg>

    <div class="brand-block">
      <span class="brand-mark"></span>
      <span class="brand-name">Tellur Works</span>
    </div>

    <div class="name-band">
      <div class="person-name">MARC OSLEN</div>
      <div class="person-role">Co-Founder</div>
    </div>

    <div class="contact-details">
      <div class="address">418 N Brindle Ave<br>Fernhollow, WI 60817</div>
      <div class="phones">+44 207 555 0148<br>07700 900412</div>
      <div class="email">dana.whitlow@qorvatfixtures.com</div>
    </div>

    <div class="icon-rail">
      <svg width="16" height="22" viewBox="0 0 16 22" aria-label="Phone"><rect x="1.5" y="1.5" width="13" height="19" rx="2.5" fill="none" stroke="#fff" stroke-width="2"/><circle cx="8" cy="17" r="1.3" fill="#fff"/></svg>
      <svg width="20" height="14" viewBox="0 0 20 14" aria-label="Email"><rect x="1" y="1" width="18" height="12" fill="none" stroke="#fff" stroke-width="2"/><path d="M1 1l9 7 9-7" fill="none" stroke="#fff" stroke-width="2"/></svg>
      <svg width="18" height="18" viewBox="0 0 18 18" aria-label="Web link"><path d="M7 11l4-4M6 8l-2 2a2.8 2.8 0 004 4l2-2M12 10l2-2a2.8 2.8 0 00-4-4L8 6" fill="none" stroke="#fff" stroke-width="2" stroke-linecap="round"/></svg>
    </div>

    <div class="web-pill">www.qorvatfixtures.com</div>
    <div class="base-stripe"></div>
  </div>
</body>
</html>
```